Stylist/Barber Standup Sign for Hair Regrowth Company

We want to design an attractive and eye-catching sign for hair stylists and barbers to sit on their workstations to attract the attention of their clients regarding hair loss and encourage them to speak to their stylist about it of they are would like to seek treatment.
50% of men and 25% of women suffer from hair loss but most are in denial that it is happening or too embarrassed to talk about it.

Copy for the flyer is as follows:

[Section 1:]
This flyer has been placed here/designed to spark conversation about hair loss

[Section 2:]
The truth is...
73% of people believe their hair is thinning
They are right

[Section 3:]
If you've got questions, your stylist or barber has answers.

Additional Background Information:

Primary target audience is men between the ages of 25-45, secondary target audience is men 46-60

Current Consumer Perception? (in the first person) “I’ve been thinking about my hair. I think it’s getting thinner and I’m scared, worried and don’t know what to do. But I don’t know if there is anything that really works. I’ve tried other things and nothing‘s worked.”

Tonality of materials? Very guy friendly, matter of fact, authoritative, its what you might hear from your best friend. Confident. Encouraging, but with a sense of urgency.

Please use our brand colors, but do not include our logo or brand name.
Colors are as follows:
Green: #4ca26f
Light Grey: #999999
Dark Grey: #262626

I have attached print templates in both PDF and Jpeg, please use those to provide final ready to print documents if you are selected.

Target Market(s)

Industry/Entity Type

Health And Wellness

Font styles to use
Sans Serif

Colors
00a990
ffffff
333333
cbcbcb

Requirements
Must have
• We want to get across the following messaging. Ideally you will submit a design using our copy and if you think you can do better, please feel free to submit another design with your own copy/messaging. If you can do it better we would love to select you :-)
• Our copy?
• This flyer has been placed here/designed to spark conversation about hair loss
• The truth is...
• 73% of people believe their hair is thinning
• They are right
• If you've got questions, your stylist or barber has answers
• Also please use our brand colors:
• Green: #4ca26f
• Light Grey: #999999
• Dark Grey: #262626
Should not have
• dont add any logos, images or ornate design. this needs to be simple, easy to ready and eye catching.
• do not use the color red in any capacity.

```html
<!DOCTYPE html>
<html lang="en">
<head>
<meta charset="utf-8">
<title>Hair Loss Conversation Standup Sign</title>
<link rel="stylesheet" href="https://fonts.googleapis.com/css2?family=Oswald:wght@300;400;500;700&family=Open+Sans:wght@300;400;600;700;800&display=swap">
<style>
  :root {
    --brand-green: #4ca26f;
    --light-grey: #999999;
    --dark-grey: #262626;
    --paper: #ffffff;
    --card-edge: #c9c9c9;
    --stage: #d6d6d6;
    --fade-1: #3a3a3a;
    --fade-2: #9a9a9a;
  }
  * { box-sizing: border-box; margin: 0; padding: 0; }
  html, body { width: 1200px; height: 960px; overflow: hidden; }
  body {
    background: var(--stage);
    display: flex;
    align-items: center;
    justify-content: center;
  }
  .sign {
    position: relative;
    width: 640px;
    height: 900px;
    background: var(--paper);
    overflow: hidden;
  }
  .sign__band {
    position: absolute;
    left: 0; right: 0; top: 0;
    height: 345px;
    background: var(--brand-green);
  }
  .sign__intro {
    position: absolute;
    top: 38px; left: 40px; right: 40px;
    text-align: center;
    font-family: "Oswald", sans-serif;
    font-weight: 400;
    font-size: 29px;
    line-height: 1.15;
    color: #f4f8f5;
  }
  .hair-card {
    position: absolute;
    top: 135px; left: 48px; right: 48px;
    height: 470px;
    background: linear-gradient(135deg, #ffffff 0%, #f6f6f6 100%);
    border: 1px solid var(--card-edge);
    border-radius: 30px;
    box-shadow: 0 4px 10px rgba(0,0,0,0.18);
    display: flex;
    flex-direction: column;
    align-items: center;
    justify-content: center;
    gap: 4px;
    font-family: "Open Sans", sans-serif;
    color: var(--dark-grey);
    text-align: center;
    line-height: 1.25;
  }
  .hair-card__line--1 { font-size: 60px; font-weight: 800; }
  .hair-card__line--2 { font-size: 54px; font-weight: 700; }
  .hair-card__line--3 { font-size: 47px; font-weight: 600; }
  .hair-card__line--4 { font-size: 41px; font-weight: 400; }
  .hair-card__line--5 { font-size: 35px; font-weight: 300; color: var(--fade-1); }
  .hair-card__line--6 { font-size: 29px; font-weight: 300; color: var(--fade-2); }
  .truth {
    position: absolute;
    top: 622px; left: 20px; right: 20px;
    text-align: center;
    font-family: "Oswald", sans-serif;
    line-height: 1.2;
  }
  .truth__title {
    font-size: 38px;
    font-weight: 700;
    color: var(--brand-green);
  }
  .truth__stat {
    font-size: 29px;
    font-weight: 400;
    color: var(--light-grey);
  }
  .truth__stat strong { font-weight: 700; color: var(--brand-green); }
  .truth__stat em { font-style: normal; color: var(--brand-green); }
  .truth__verdict {
    font-size: 30px;
    font-weight: 700;
    color: var(--light-grey);
  }
  .sign__footer {
    position: absolute;
    left: 0; right: 0; bottom: 0;
    height: 92px;
    background: var(--dark-grey);
    display: flex;
    align-items: center;
    justify-content: center;
    font-family: "Oswald", sans-serif;
    font-weight: 300;
    font-size: 17px;
    letter-spacing: 2px;
    color: #e6e6e6;
  }
</style>
</head>
<body>
  <main class="sign">
    <div class="sign__band"></div>
    <p class="sign__intro">This flyer has been placed here/designed to<br>spark conversation about hair loss</p>

    <section class="hair-card" aria-label="Your hair, fading">
      <p class="hair-card__line--1">YOUR HAIR</p>
      <p class="hair-card__line--2">YOUR HAIR</p>
      <p class="hair-card__line--3">YOUR HAIR</p>
      <p class="hair-card__line--4">YOUR HAIR</p>
      <p class="hair-card__line--5">YOUR HAIR</p>
      <p class="hair-card__line--6">YOUR HAIR</p>
    </section>

    <section class="truth">
      <h2 class="truth__title">The Truth Is...</h2>
      <p class="truth__stat"><strong>73% of people</strong> believe their hair is <em>thinning</em></p>
      <p class="truth__verdict">THEY ARE RIGHT</p>
    </section>

    <footer class="sign__footer">If you've got questions, your stylist or barber has answers.</footer>
  </main>
</body>
</html>
```